Business Card

Need a clean, professional, simple, but clever business card for our company ZOLT RIDES. We only want to see black and white colors as that reflects the branding of our company. Attaching logo. Will also consider the "sky blue" shown in our web site sample png - but use of the color should be minimal.

Zolt Rides is a executive car service operating in cities throughout Africa. By operating well equipped Vantorel Kess vehicles, we offer the smoothest and stylish ride in town. We aim to provide customers with a valuable experience. That’s why we make sure our patrons get picked up like a boss, travel in style, and Travel Refined.

We need a card that says that. Likely to print on the best quality/smoothest paper available, as it must speak volumes of our business and class.

We would like the rear of the card to be all black. Perhaps we can put the web url on it, or leave it blank if it looks neater/more elegant.

Use the following contact information (as you see fit):

Zolt Rides Limited
P.O. Box 58146
Dar es Salaam, Tanzania

Baraka Nyerenda
Managing Director

+255 (0) 754 829067
sales@zoltrides.example

web url: www.zoltrides.example
email: chauffeur@zoltrides.example

***Winning designer will likely be commissioned for more promotional work in near future.

Target Market(s)

The target market for this card is corporate executives of top firms (financial, consulting, businessmen, etc). They are interested in high quality transportation. Our fleet is all high end Vantorel Kess black cars (black exterior, black interior); and therefore, that high end quality and promptness must be reflected in the card. Also simplicity, as we we take care of all the little details behind the scene.

Industry/Entity Type

Business

Requirements
Must have
• Font must be: Helvetica Neue, like the logo. You may use other variations (Thin, Ultra thin, Regular, Bold), so long as it looks and prints well.

If web url is included on the back of the card, then do NOT include it also on the front.
Nice to have
• If there is something nice and clever that you can do/think of that doesn't make the card look busy, but adds a little "posh", then I could be even more interested.

However, if there's no little thing do be done, I'd rather a simple, but very professional looking card that attracts a lot of attention.

```html
<!DOCTYPE html>
<html lang="en">
<head>
<meta charset="utf-8">
<title>Zolt Rides — Business Card</title>
<link rel="stylesheet" href="https://fonts.googleapis.com/css2?family=Inter:wght@300;400;600;700&display=swap">
<style>
  :root {
    --page-bg: #e9e9ea;
    --card-white: #ffffff;
    --card-black: #0b0f1a;
    --ink: #1b1b1d;
    --ink-soft: #5a5a5e;
    --sky: #2aa7c9;
  }
  * { margin: 0; padding: 0; box-sizing: border-box; }
  html, body {
    width: 1200px;
    height: 900px;
    overflow: hidden;
    background: var(--page-bg);
    font-family: "Inter", "Helvetica Neue", Arial, sans-serif;
  }
  .canvas {
    position: relative;
    width: 1200px;
    height: 900px;
  }
  .card {
    position: absolute;
    left: 320px;
    width: 560px;
    height: 320px;
    box-shadow: 0 10px 30px rgba(0,0,0,0.18);
  }
  .card-back {
    top: 80px;
    background: var(--card-black);
  }
  .card-back .web-url {
    position: absolute;
    right: 30px;
    bottom: 26px;
    font-size: 15px;
    font-weight: 300;
    letter-spacing: 0.02em;
    color: var(--sky);
  }
  .card-front {
    top: 500px;
    background: var(--card-white);
    color: var(--ink);
  }
  .brand {
    position: absolute;
    left: 40px;
    top: 44px;
  }
  .brand-name {
    font-size: 40px;
    font-weight: 300;
    letter-spacing: 0.06em;
    line-height: 1;
    color: var(--ink);
  }
  .brand-tagline {
    margin-top: 6px;
    font-size: 17px;
    font-weight: 300;
    color: var(--ink-soft);
  }
  .person {
    position: absolute;
    left: 40px;
    top: 160px;
    font-size: 15px;
    line-height: 1.3;
  }
  .person-name { color: var(--sky); font-weight: 600; }
  .person-title { color: var(--ink-soft); font-weight: 400; }
  .contact {
    position: absolute;
    left: 40px;
    top: 240px;
    font-size: 15px;
    line-height: 1.35;
    color: var(--ink-soft);
    list-style: none;
  }
  .contact-label {
    display: inline-block;
    width: 20px;
    font-weight: 700;
    color: var(--ink);
  }
  .company-address {
    position: absolute;
    left: 330px;
    top: 160px;
    font-style: normal;
    font-size: 15px;
    line-height: 1.3;
    color: var(--ink-soft);
  }
  .company-name { font-weight: 600; color: var(--ink); }
</style>
</head>
<body>
<main class="canvas">
  <section class="card card-back" aria-label="Card back">
    <p class="web-url">www.zoltrides.example</p>
  </section>

  <section class="card card-front" aria-label="Card front">
    <header class="brand">
      <h1 class="brand-name">ZOLT RIDES</h1>
      <p class="brand-tagline">Travel Refined.</p>
    </header>

    <div class="person">
      <p class="person-name">Baraka Nyerenda</p>
      <p class="person-title">Managing Director</p>
    </div>

    <ul class="contact">
      <li><span class="contact-label">p</span>+255 (0) 754 829 067</li>
      <li><span class="contact-label">e</span>sales@zoltrides.example</li>
    </ul>

    <address class="company-address">
      <p class="company-name">Zolt Rides Limited</p>
      <p>P.O. Box 58146</p>
      <p>Dar es Salaam, Tanzania</p>
    </address>
  </section>
</main>
</body>
</html>
```